Stationery Design Project

We are looking for a full revision of our existing stationary to include within this project:

- Letterhead
- Business card
- Compliment slip

The items should be a reflection of our new website which can be found at http://www.larkfieldchecks.co.uk/

Our logo files are included within the file brief

There are some further projects which we may approach the winning designer for as we need a revision to the front cover of our reports, a new price list and two brochures for specific target markets.

Industry/Entity Type

Business

```html
<!DOCTYPE html>
<html lang="en">
<head>
<meta charset="utf-8">
<title>Larkfield Checks — Stationery</title>
<link href="https://fonts.googleapis.com/css2?family=PT+Sans:wght@400;700&family=Parisienne&display=swap" rel="stylesheet">
<style>
  :root {
    --backdrop: #ececec;
    --paper: #fbfbfb;
    --brand-blue: #2559b3;
    --brand-navy: #1c2a78;
    --brand-green: #6cb33f;
    --ink: #3a3a3a;
    --ink-soft: #5a5a5a;
  }
  * { box-sizing: border-box; margin: 0; padding: 0; }
  html, body {
    width: 1200px; height: 795px; overflow: hidden;
    background: var(--backdrop);
    font-family: "PT Sans", Arial, sans-serif;
    color: var(--ink);
  }
  .sheet {
    position: absolute; background: var(--paper);
    box-shadow: 0 2px 6px rgba(0,0,0,.12);
  }
  .band-top { position: absolute; left: 0; right: 0; top: 0; background: var(--brand-blue); }
  .band-foot { position: absolute; left: 0; right: 0; }
  .band-foot .green { height: 3px; background: var(--brand-green); }
  .band-foot .navy { background: var(--brand-navy); }
  .wordmark {
    position: absolute; color: var(--brand-navy); font-weight: 700;
    white-space: nowrap; display: flex; align-items: center; gap: 6px;
  }
  .wordmark .dot { width: .55em; height: .55em; border-radius: 50%; background: var(--brand-blue); }
  .contact-list { list-style: none; }
  .contact-list li { display: flex; align-items: center; gap: 5px; }
  .contact-list .icon { width: 7px; height: 7px; background: var(--brand-green); flex: none; }
  .contact-list .web { font-weight: 700; }

  /* Letterhead */
  .letterhead { left: 120px; top: 80px; width: 450px; height: 636px; }
  .letterhead .band-top { height: 8px; }
  .letter-body { position: absolute; left: 70px; top: 150px; width: 320px; font-size: 8.4px; line-height: 1.45; color: var(--ink-soft); }
  .letter-body .salutation { font-weight: 700; color: var(--ink); margin-bottom: 8px; }
  .letter-body p { margin-bottom: 9px; }
  .signature { position: absolute; left: 70px; top: 470px; }
  .signature .sign { font-family: "Parisienne", cursive; font-size: 28px; color: #333; line-height: 1; }
  .signature .role { font-size: 8.5px; font-weight: 700; color: var(--ink-soft); margin-top: 2px; }
  .letterhead .wordmark { left: 40px; bottom: 44px; font-size: 19px; }
  .letterhead .contact-list { position: absolute; left: 250px; bottom: 46px; font-size: 7px; line-height: 1.6; }
  .letterhead .address { position: absolute; right: 30px; bottom: 49px; font-size: 7px; line-height: 1.5; text-align: right; }
  .letterhead .band-foot { bottom: 12px; }
  .letterhead .band-foot .navy { height: 10px; }

  /* Cards */
  .card { width: 380px; height: 216px; left: 690px; }
  .card .band-top { height: 7px; }
  .card .band-foot { bottom: 10px; }
  .card .band-foot .navy { height: 9px; }
  .card-front { top: 130px; }
  .card-front .wordmark { right: 22px; top: 30px; font-size: 15px; }
  .holder { position: absolute; left: 26px; top: 86px; }
  .holder .name { font-size: 15px; color: var(--ink); }
  .holder .title { font-size: 9px; color: var(--ink-soft); margin-bottom: 9px; }
  .card-front .contact-list { font-size: 8px; line-height: 1.55; }
  .card-front .address { margin-top: 7px; font-size: 8px; line-height: 1.45; }
  .card-back { top: 420px; }
  .card-back .wordmark { left: 50%; top: 50%; transform: translate(-50%, -60%); font-size: 24px; }
</style>
</head>
<body>

<section class="sheet letterhead" aria-label="Letterhead">
  <div class="band-top"></div>
  <div class="letter-body">
    <p class="salutation">Lorem Ipsum,</p>
    <p>Cras mattis consectetur purus sit amet fermentum. Etiam porta sem malesuada magna mollis euismod. Integer posuere erat a ante venenatis dapibus posuere velit aliquet. Cras justo odio, dapibus ac facilisis in, egestas eget quam. Aenean eu leo quam. Pellentesque ornare sem lacinia quam venenatis vestibulum.</p>
    <p>Vivamus sagittis lacus vel augue laoreet rutrum faucibus dolor auctor. Donec sed odio dui. Etiam porta sem malesuada magna mollis euismod. Morbi leo risus, porta ac consectetur ac, vestibulum at eros. Nullam id dolor id nibh ultricies vehicula ut id elit.</p>
    <p>Donec id elit non mi porta gravida at eget metus. Fusce dapibus, tellus ac cursus commodo, tortor mauris condimentum nibh, ut fermentum massa justo sit amet risus. Cras justo odio, dapibus ac facilisis in, egestas eget quam. Cum sociis natoque penatibus et magnis dis parturient montes, nascetur ridiculus mus.</p>
    <p>Cum sociis natoque penatibus et magnis dis parturient montes, nascetur ridiculus mus. Curabitur blandit tempus porttitor. Aenean lacinia bibendum nulla sed consectetur. Lorem ipsum dolor sit amet, consectetur adipiscing elit.</p>
    <p>Cras justo odio, dapibus ac facilisis in, egestas eget quam. Morbi leo risus, porta ac consectetur ac, vestibulum at eros. Duis mollis, est non commodo luctus, nisi erat porttitor ligula, eget lacinia odio sem nec elit. Integer posuere erat a ante venenatis dapibus posuere velit aliquet. Vivamus sagittis lacus vel augue laoreet rutrum faucibus dolor auctor.</p>
  </div>
  <div class="signature">
    <div class="sign">Your Name</div>
    <div class="role">Company Director</div>
  </div>
  <div class="wordmark"><span class="dot"></span>Larkfield Checks</div>
  <ul class="contact-list">
    <li><span class="icon"></span>08450 762 418</li>
    <li><span class="icon"></span>mail@larkfieldchecks.co.uk</li>
    <li class="web"><span class="icon"></span>www.larkfieldchecks.co.uk</li>
  </ul>
  <div class="address">14 Harrow Lane<br>Ashford, SC 29611</div>
  <div class="band-foot"><div class="green"></div><div class="navy"></div></div>
</section>

<section class="sheet card card-front" aria-label="Business card, front">
  <div class="band-top"></div>
  <div class="wordmark"><span class="dot"></span>Larkfield Checks</div>
  <div class="holder">
    <div class="name">Dana Whitcombe</div>
    <div class="title">Chief Inspector</div>
    <ul class="contact-list">
      <li><span class="icon"></span>08450 762 418</li>
      <li><span class="icon"></span>mail@larkfieldchecks.co.uk</li>
      <li class="web"><span class="icon"></span>www.larkfieldchecks.co.uk</li>
    </ul>
    <div class="address">14 Harrow Lane<br>Ashford, SC 29611</div>
  </div>
  <div class="band-foot"><div class="green"></div><div class="navy"></div></div>
</section>

<section class="sheet card card-back" aria-label="Business card, back">
  <div class="band-top"></div>
  <div class="wordmark"><span class="dot"></span>Larkfield Checks</div>
  <div class="band-foot"><div class="green"></div><div class="navy"></div></div>
</section>

</body>
</html>
```